KLWB Canberra Pty Ltd

Want something creative and that catches your eye. We are a traffic control companythat offers all aspects of traffic control from planning to roadworks.

Contact Information for Business Card

Dean Morrow - Director
Ph: 0419 583 216
Email: dean@klwb.com.au
27 Vane Harbin ct Larwood ACT 2908

```html
<!DOCTYPE html>
<html lang="en">
<head>
<meta charset="utf-8">
<title>KLWB Canberra – Business Card</title>
<link rel="stylesheet" href="https://fonts.googleapis.com/css2?family=Roboto:wght@300;400;700;900&display=swap">
<style>
  :root {
    --stage: #3b3b3b;
    --card: #262a22;
    --band: #d5d5d3;
    --band-edge: #9a9a98;
    --ink-dark: #1c1c1c;
    --ink-light: #f2f2ee;
    --accent-green: #9bd06b;
    --accent-orange: #e9a463;
    --accent-yellow: #e8c46b;
    --accent-grey: #b8b8b6;
  }
  * { box-sizing: border-box; margin: 0; padding: 0; }
  html, body { width: 1200px; height: 646px; overflow: hidden; }
  body {
    background: var(--stage);
    font-family: "Roboto", Arial, sans-serif;
    position: relative;
  }
  .card {
    position: absolute;
    top: 173px;
    width: 525px;
    height: 300px;
    background: var(--card);
    overflow: hidden;
    box-shadow: 0 12px 30px rgba(0,0,0,.45);
  }
  .card--back { left: 50px; }
  .card--front { left: 625px; }
  .pattern-field {
    position: absolute;
    inset: 0;
    width: 100%;
    height: 100%;
  }

  /* Back side */
  .services {
    position: absolute;
    left: 160px;
    top: 78px;
    width: 255px;
    text-align: right;
    color: var(--ink-light);
    font-weight: 300;
    font-size: 12.5px;
    line-height: 1.5;
  }

  /* Front side */
  .name-band {
    position: absolute;
    left: 245px;
    top: 26px;
    width: 280px;
    height: 54px;
    background: var(--band);
    border-top: 4px solid var(--band-edge);
    display: flex;
    align-items: center;
    justify-content: flex-end;
    padding-right: 26px;
  }
  .name-band__name {
    font-weight: 900;
    font-size: 29px;
    color: var(--ink-dark);
    letter-spacing: .2px;
  }
  .role-tag {
    position: absolute;
    right: 62px;
    top: 84px;
    background: var(--band);
    color: var(--ink-dark);
    font-size: 10px;
    font-weight: 400;
    padding: 2px 10px;
  }
  .contact-list {
    position: absolute;
    left: 30px;
    top: 150px;
    list-style: none;
    color: var(--ink-light);
    font-weight: 300;
    font-size: 12.5px;
    line-height: 1.7;
  }
  .contact-list li { display: flex; align-items: center; gap: 8px; }
  .contact-list svg { width: 11px; height: 11px; flex: none; }
  .brand {
    position: absolute;
    left: 30px;
    bottom: 26px;
    display: flex;
    align-items: center;
    gap: 8px;
  }
  .brand__mark {
    width: 18px; height: 18px;
    border-radius: 50%;
    background: var(--accent-orange);
  }
  .brand__name {
    color: var(--ink-light);
    font-weight: 700;
    font-size: 20px;
  }
</style>
</head>
<body>

<section class="card card--back" aria-label="Business card, reverse side">
  <svg class="pattern-field" viewBox="0 0 525 300" role="img" aria-label="Honeycomb pattern of green, orange, yellow and grey hexagons">
    <defs>
      <linearGradient id="hexToneA" x1="0" y1="0" x2="1" y2="1">
        <stop offset="0" stop-color="#e8c46b"/>
        <stop offset=".35" stop-color="#9bd06b"/>
        <stop offset=".7" stop-color="#e9a463"/>
        <stop offset="1" stop-color="#b8b8b6"/>
      </linearGradient>
      <linearGradient id="hexToneB" x1="0" y1="0" x2="1" y2="1">
        <stop offset="0" stop-color="#b8b8b6"/>
        <stop offset=".4" stop-color="#9bd06b"/>
        <stop offset=".75" stop-color="#e8c46b"/>
        <stop offset="1" stop-color="#e9a463"/>
      </linearGradient>
    </defs>
    <polygon fill="url(#hexToneA)" points="230,0 525,0 525,190 490,200 455,180 432,150 428,90 405,68 330,58 270,45 240,25"/>
    <polygon fill="url(#hexToneB)" points="0,170 40,160 75,185 105,205 125,235 150,255 175,300 0,300"/>
  </svg>
  <p class="services">
    Industrial Relations &amp; Employment Accredited for ACT | Capital Grid Accredited | Southern Power | Emergency Response Vehicles | 24 Hour Service | TTM Planning &amp; Design for ACT | Traffic Management Planning &amp; Design | Traffic Engineering Consultants | Traffic Control | Civic Roads Accredited | NRT Accredited | Council Approval | Traffic Management Consultants | BCWU-EBA
  </p>
</section>

<section class="card card--front" aria-label="Business card, front side">
  <svg class="pattern-field" viewBox="0 0 525 300" role="img" aria-label="Honeycomb pattern of green, orange, yellow and grey hexagons">
    <defs>
      <linearGradient id="hexToneC" x1="0" y1="0" x2="1" y2="1">
        <stop offset="0" stop-color="#e9a463"/>
        <stop offset=".3" stop-color="#9bd06b"/>
        <stop offset=".6" stop-color="#e8c46b"/>
        <stop offset=".85" stop-color="#b8b8b6"/>
        <stop offset="1" stop-color="#9bd06b"/>
      </linearGradient>
    </defs>
    <polygon fill="url(#hexToneC)" points="175,40 235,30 245,100 320,105 380,130 430,165 465,215 440,265 385,290 335,255 300,215 265,170 215,135 185,95"/>
  </svg>

  <div class="name-band">
    <h1 class="name-band__name">Dean Morrow</h1>
  </div>
  <p class="role-tag">Director</p>

  <ul class="contact-list">
    <li>
      <svg viewBox="0 0 12 12" aria-hidden="true"><path fill="#9bd06b" d="M2.5 1h2l1 2.5-1.3 1a6 6 0 0 0 3.3 3.3l1-1.3L11 7.5v2c0 .8-.7 1.5-1.5 1.5A8.5 8.5 0 0 1 1 2.5C1 1.7 1.7 1 2.5 1z"/></svg>
      0419 583 216
    </li>
    <li>
      <svg viewBox="0 0 12 12" aria-hidden="true"><rect x="1" y="2.5" width="10" height="7" fill="#9bd06b"/><path d="M1 2.5l5 4 5-4" stroke="#262a22" fill="none"/></svg>
      dean@klwb.com.au
    </li>
    <li>
      <svg viewBox="0 0 12 12" aria-hidden="true"><path fill="#9bd06b" d="M6 .5a4 4 0 0 0-4 4c0 3 4 7 4 7s4-4 4-7a4 4 0 0 0-4-4zm0 5.5a1.5 1.5 0 1 1 0-3 1.5 1.5 0 0 1 0 3z"/></svg>
      27 Vane Harbin ct Larwood ACT 2908
    </li>
  </ul>

  <div class="brand">
    <span class="brand__mark" aria-hidden="true"></span>
    <span class="brand__name">KLWB Canberra</span>
  </div>
</section>

</body>
</html>
```